Video Company website for high tech video software company

Design a website for a software company that has an extensive list of products that process incoming TV video and video ads and processes the video for delivery to mobile phones, tablets, Set Top Boxes, and PCs.

Coded - Design and coding required

1 page

```html
<!DOCTYPE html>
<html lang="en">
<head>
<meta charset="utf-8">
<title>StreamVault – OTT IPTV DVB Complete Solution</title>
<link rel="stylesheet" href="https://fonts.googleapis.com/css2?family=Poppins:wght@400;500;600;700&display=swap">
<style>
  :root{
    --canvas:#ffffff;
    --night:#000000;
    --deep:#0b0f24;
    --haze:#1a2340;
    --ink:#111111;
    --white:#ffffff;
    --muted:#c9ccd6;
    --accent:#2ba9ea;
    --accent-glow:#3fd0ff;
    --violet:#5b3bd6;
    --outline:#5b6172;
  }
  *{box-sizing:border-box;margin:0;padding:0}
  html,body{width:1200px;height:1013px;overflow:hidden;background:var(--canvas)}
  body{position:relative;font-family:"Poppins",sans-serif;color:var(--white)}
  .page{position:absolute;top:72px;width:539px;height:878px;overflow:hidden;background:var(--night)}
  .page--light-cards{left:45px}
  .page--outline-cards{left:616px}
  .backdrop{position:absolute;left:0;top:0;width:100%}
  .page--light-cards .backdrop{height:440px;background:
      radial-gradient(ellipse 60% 45% at 30% 30%,rgba(60,80,120,.45),transparent 70%),
      radial-gradient(ellipse 50% 40% at 75% 25%,rgba(70,30,60,.35),transparent 70%),
      linear-gradient(180deg,var(--deep) 0%,#080a18 70%,var(--night) 100%)}
  .page--outline-cards .backdrop{height:100%;background:
      radial-gradient(ellipse 60% 25% at 30% 16%,rgba(60,80,120,.45),transparent 70%),
      radial-gradient(ellipse 45% 20% at 80% 14%,rgba(70,30,60,.35),transparent 70%),
      radial-gradient(ellipse 55% 25% at 30% 75%,rgba(40,70,90,.35),transparent 70%),
      radial-gradient(ellipse 40% 20% at 85% 90%,rgba(40,60,90,.3),transparent 70%),
      linear-gradient(180deg,var(--deep) 0%,#070916 40%,#05060f 100%)}

  .brand{position:absolute;font-weight:700;color:var(--white);letter-spacing:.2px;display:flex;align-items:center;gap:5px}
  .brand__dot{width:7px;height:7px;background:var(--accent);border-radius:50%}
  .brand--header{left:101px;top:18px;font-size:13px}
  .nav{position:absolute;font-size:7.6px;font-weight:600;display:flex}
  .nav--header{left:296px;top:22px;gap:19px}
  .hero-title{position:absolute;left:0;width:539px;top:88px;text-align:center;font-weight:700;font-size:22px;line-height:27px;letter-spacing:.2px}

  .diagram{position:absolute;left:0;top:185px;width:539px;height:150px}
  .d-label{position:absolute;transform:translateX(-50%);font-size:7.3px;font-weight:600;text-align:center;line-height:8.5px;white-space:nowrap}
  .d-icon{position:absolute;width:26px;height:26px;transform:translateX(-50%);color:var(--white)}
  .beam{position:absolute;left:104px;top:64px;width:300px;height:13px;border-radius:3px;
    background:linear-gradient(90deg,#0a5fa8,var(--accent-glow) 15%,#0b7ad0 30%,var(--accent-glow) 50%,#0a68b6 65%,var(--accent-glow) 80%,#1c5aa0)}
  .dish{position:absolute;left:55px;top:48px;width:38px;height:44px;border-radius:6px;background:linear-gradient(160deg,#f2f4f8,var(--accent))}
  .devices{position:absolute;left:395px;top:5px;width:92px;height:126px;border-radius:10px;
    background:radial-gradient(ellipse at 30% 50%,var(--violet),#2a1a6a 55%,rgba(40,40,60,.7) 100%)}

  .card{position:absolute;width:107px;height:104px;text-align:center}
  .page--light-cards .card{background:var(--white);border-radius:3px;color:var(--ink)}
  .page--outline-cards .card{color:var(--white)}
  .card__frame{position:absolute;inset:0;width:107px;height:104px}
  .card__icon{position:absolute;left:39.5px;top:12px;width:28px;height:28px}
  .card__title{position:absolute;left:0;right:0;top:47px;font-size:11px;font-weight:500}
  .card__text{position:absolute;left:0;right:0;top:66px;font-size:6.3px;line-height:9px}
  .page--outline-cards .card__text{color:var(--muted)}
  .col1{left:101px}.col2{left:215px}.col3{left:330px}
  .row1{top:371px}.row2{top:491px}.row3{top:615px}

  .brand--footer{left:0;width:539px;justify-content:center;top:768px;font-size:13px}
  .page--outline-cards .brand--footer{left:219px;width:101px;height:40px;top:757px;background:var(--night)}
  .nav--footer{left:0;width:539px;justify-content:center;top:802px;gap:19px}
  .copyright{position:absolute;left:0;width:539px;top:825px;text-align:center;font-size:6.4px}
</style>
</head>
<body>

<svg width="0" height="0" style="position:absolute" aria-hidden="true">
  <defs>
    <symbol id="i-tick" viewBox="0 0 24 24"><circle cx="12" cy="12" r="7" fill="none" stroke="currentColor" stroke-width="1.4"/><path d="M8.5 12l2.5 2.5 5-5" fill="none" stroke="currentColor" stroke-width="1.6"/></symbol>
    <symbol id="i-globe" viewBox="0 0 24 24"><g fill="none" stroke="currentColor" stroke-width="1.3"><circle cx="12" cy="12" r="7.5"/><ellipse cx="12" cy="12" rx="3.3" ry="7.5"/><path d="M4.5 12h15M6 8h12M6 16h12"/></g></symbol>
    <symbol id="i-headset" viewBox="0 0 24 24"><g fill="none" stroke="currentColor" stroke-width="1.3"><path d="M7 12a5 5 0 0 1 10 0"/><rect x="6" y="11.5" width="2.4" height="4" rx="1"/><rect x="15.6" y="11.5" width="2.4" height="4" rx="1"/><path d="M8 19a4 3 0 0 1 8 0"/></g></symbol>
    <symbol id="i-shield" viewBox="0 0 24 24"><g fill="none" stroke="currentColor" stroke-width="1.4"><path d="M12 4l6.5 2.5v5c0 4-3 6.8-6.5 8.5-3.5-1.7-6.5-4.5-6.5-8.5v-5z"/><path d="M9 12l2.2 2.2L15 10.4"/></g></symbol>
    <symbol id="i-live" viewBox="0 0 24 24"><g fill="none" stroke="currentColor" stroke-width="1.2"><rect x="4.5" y="11" width="15" height="7" rx="1.2"/><circle cx="12" cy="7" r="1"/><path d="M9.5 4.8a3.5 3.5 0 0 0 0 4.4M14.5 4.8a3.5 3.5 0 0 1 0 4.4"/></g><text x="12" y="16.6" font-family="Poppins,sans-serif" font-size="5" font-weight="700" text-anchor="middle" fill="currentColor">LIVE</text></symbol>
    <symbol id="i-cloudplay" viewBox="0 0 24 24"><g fill="none" stroke="currentColor" stroke-width="1.3"><path d="M7 18h10a3.5 3.5 0 0 0 0-7 5 5 0 0 0-9.6 1.2A3 3 0 0 0 7 18z"/><path d="M11 12.5v4l3.2-2z" fill="currentColor"/><path d="M16 6.5a3 3 0 0 1 2.5 2.5M17 4.5a5 5 0 0 1 3.5 3.5"/></g></symbol>
    <symbol id="i-ad" viewBox="0 0 24 24"><g fill="none" stroke="currentColor" stroke-width="1.3"><rect x="4.5" y="6" width="15" height="10" rx="2"/><path d="M12 16v3M9 19h6"/></g><text x="12" y="13.8" font-family="Poppins,sans-serif" font-size="6" font-weight="700" text-anchor="middle" fill="currentColor">AD</text></symbol>
    <symbol id="i-cloudnet" viewBox="0 0 24 24"><g fill="none" stroke="currentColor" stroke-width="1.3"><path d="M7 14h10a3 3 0 0 0 0-6 4.5 4.5 0 0 0-8.7 1A2.6 2.6 0 0 0 7 14z"/><path d="M8 14v3M12 14v4M16 14v3"/><circle cx="8" cy="18" r="1"/><circle cx="12" cy="19" r="1"/><circle cx="16" cy="18" r="1"/></g></symbol>
    <symbol id="i-sms" viewBox="0 0 24 24"><path d="M5 7h14v9h-8l-4 3v-3H5z" fill="none" stroke="currentColor" stroke-width="1.3"/><text x="12" y="13.6" font-family="Poppins,sans-serif" font-size="4.6" font-weight="600" text-anchor="middle" fill="currentColor">sms</text></symbol>
    <symbol id="i-userplus" viewBox="0 0 24 24"><g fill="none" stroke="currentColor" stroke-width="1.4"><circle cx="10" cy="8" r="4"/><path d="M3.5 20a6.5 6.5 0 0 1 9.5-5.8M17 13v7M13.5 16.5h7"/></g></symbol>
    <symbol id="i-app" viewBox="0 0 24 24"><g fill="none" stroke="currentColor" stroke-width="1.4"><rect x="7" y="3.5" width="10" height="17" rx="1.5"/><path d="M9.5 7.5h2v2h-2zM12.5 7.5h2v2h-2zM9.5 11h2v2h-2zM12.5 11h2v2h-2z"/></g></symbol>
    <symbol id="frame" viewBox="0 0 107 104"><path d="M11 1.5h85l9.5 101H1.5z" fill="rgba(0,0,0,.25)" stroke="#5b6172" stroke-width="1.2" stroke-linejoin="round"/></symbol>
    <symbol id="badge" viewBox="0 0 28 28"><circle cx="14" cy="14" r="14" fill="#2ba9ea"/></symbol>
  </defs>
</svg>

<!-- Variant A: white feature cards -->
<section class="page page--light-cards">
  <div class="backdrop" role="img" aria-label="Dark space scene with satellites over the earth"></div>
  <div class="brand brand--header"><span>StreamVault</span><span class="brand__dot"></span></div>
  <nav class="nav nav--header"><span>Products</span><span>Resources</span><span>Contact</span></nav>
  <h1 class="hero-title">OTT IPTV DVB<br>COMPLETE SOLUTION</h1>

  <div class="diagram">
    <div class="dish" role="img" aria-label="Satellite dish receiving signal"></div>
    <div class="beam" role="img" aria-label="Video signal flowing to devices"></div>
    <div class="devices" role="img" aria-label="Phones, tablets, set top boxes and PCs receiving the stream"></div>
    <svg class="d-icon" style="left:131px;top:12px"><use href="#i-cloudplay"/></svg><div class="d-label" style="left:131px;top:40px">Transcoding</div>
    <svg class="d-icon" style="left:213px;top:5px"><use href="#i-userplus"/></svg><div class="d-label" style="left:213px;top:33px">Subscriber<br>Management</div>
    <svg class="d-icon" style="left:300px;top:10px"><use href="#i-live"/></svg><div class="d-label" style="left:300px;top:40px">Streaming</div>
    <svg class="d-icon" style="left:370px;top:11px"><use href="#i-app"/></svg><div class="d-label" style="left:370px;top:40px">Apps</div>
    <div class="d-label" style="left:165px;top:101px">Middleware</div><svg class="d-icon" style="left:165px;top:113px"><use href="#i-cloudnet"/></svg>
    <div class="d-label" style="left:254px;top:96px">CAS/DRM<br>Security</div><svg class="d-icon" style="left:254px;top:114px"><use href="#i-shield"/></svg>
    <div class="d-label" style="left:350px;top:96px">Targeted<br>Ads</div><svg class="d-icon" style="left:350px;top:113px"><use href="#i-ad"/></svg>
  </div>

  <article class="card col1 row1"><svg class="card__icon"><use href="#badge"/></svg><svg class="card__icon" style="color:#fff"><use href="#i-tick"/></svg><h3 class="card__title">Complete</h3><p class="card__text">Apps with Live TV<br>Catchup TV + VOD<br>Middleware + Ads</p></article>
  <article class="card col2 row1"><svg class="card__icon"><use href="#badge"/></svg><svg class="card__icon" style="color:#fff"><use href="#i-globe"/></svg><h3 class="card__title">MSO Scale</h3><p class="card__text">Nationwide Distribution<br>Cloud or on premise<br>Distributed head-ends</p></article>
  <article class="card col3 row1"><svg class="card__icon"><use href="#badge"/></svg><svg class="card__icon" style="color:#fff"><use href="#i-headset"/></svg><h3 class="card__title">Reliable</h3><p class="card__text">24/7 Operation<br>24/7 System Monitoring<br>MPEG Video Inspection</p></article>
  <article class="card col1 row2"><svg class="card__icon"><use href="#badge"/></svg><svg class="card__icon" style="color:#fff"><use href="#i-shield"/></svg><h3 class="card__title">CAS / DRM</h3><p class="card__text">Hollywood approved<br>Highly secure for<br>IPTV/OTT/DVB systems</p></article>
  <article class="card col2 row2"><svg class="card__icon"><use href="#badge"/></svg><svg class="card__icon" style="color:#fff"><use href="#i-live"/></svg><h3 class="card__title">Streaming</h3><p class="card__text">High Capacity<br>Edge Caching<br>No 3rd party CDN needed</p></article>
  <article class="card col3 row2"><svg class="card__icon"><use href="#badge"/></svg><svg class="card__icon" style="color:#fff"><use href="#i-cloudplay"/></svg><h3 class="card__title">Transcoding</h3><p class="card__text">High Quality<br>High Density<br>4K/8K Full HD &amp; SD</p></article>
  <article class="card col1 row3"><svg class="card__icon"><use href="#badge"/></svg><svg class="card__icon" style="color:#fff"><use href="#i-ad"/></svg><h3 class="card__title">Advertising</h3><p class="card__text">Targeted Ads<br>Ad analytics<br>Advertiser Portal</p></article>
  <article class="card col2 row3"><svg class="card__icon"><use href="#badge"/></svg><svg class="card__icon" style="color:#fff"><use href="#i-cloudnet"/></svg><h3 class="card__title">Middleware</h3><p class="card__text">Live TV with EPG<br>VOD + CDN<br>Catchup TV</p></article>
  <article class="card col3 row3"><svg class="card__icon"><use href="#badge"/></svg><svg class="card__icon" style="color:#fff"><use href="#i-sms"/></svg><h3 class="card__title">SMS</h3><p class="card__text">MSO Grade Subscriber<br>Management<br>for IPTV/OTT/DVB</p></article>

  <div class="brand brand--footer"><span>StreamVault</span><span class="brand__dot"></span></div>
  <nav class="nav nav--footer"><span>Products</span><span>Resources</span><span>Contact</span></nav>
  <p class="copyright">Copyright © 2021 All Right Reserved</p>
</section>

<!-- Variant B: outlined feature cards -->
<section class="page page--outline-cards">
  <div class="backdrop" role="img" aria-label="Dark space scene with satellites continuing down the page"></div>
  <div class="brand brand--header"><span>StreamVault</span><span class="brand__dot"></span></div>
  <nav class="nav nav--header"><span>Products</span><span>Resources</span><span>Contact</span></nav>
  <h1 class="hero-title">OTT IPTV DVB<br>COMPLETE SOLUTION</h1>

  <div class="diagram">
    <div class="dish" role="img" aria-label="Satellite dish receiving signal"></div>
    <div class="beam" role="img" aria-label="Video signal flowing to devices"></div>
    <div class="devices" role="img" aria-label="Phones, tablets, set top boxes and PCs receiving the stream"></div>
    <svg class="d-icon" style="left:131px;top:12px"><use href="#i-cloudplay"/></svg><div class="d-label" style="left:131px;top:40px">Transcoding</div>
    <svg class="d-icon" style="left:213px;top:5px"><use href="#i-userplus"/></svg><div class="d-label" style="left:213px;top:33px">Subscriber<br>Management</div>
    <svg class="d-icon" style="left:300px;top:10px"><use href="#i-live"/></svg><div class="d-label" style="left:300px;top:40px">Streaming</div>
    <svg class="d-icon" style="left:370px;top:11px"><use href="#i-app"/></svg><div class="d-label" style="left:370px;top:40px">Apps</div>
    <div class="d-label" style="left:165px;top:101px">Middleware</div><svg class="d-icon" style="left:165px;top:113px"><use href="#i-cloudnet"/></svg>
    <div class="d-label" style="left:254px;top:96px">CAS/DRM<br>Security</div><svg class="d-icon" style="left:254px;top:114px"><use href="#i-shield"/></svg>
    <div class="d-label" style="left:350px;top:96px">Targeted<br>Ads</div><svg class="d-icon" style="left:350px;top:113px"><use href="#i-ad"/></svg>
  </div>

  <article class="card col1 row1"><svg class="card__frame"><use href="#frame"/></svg><svg class="card__icon"><use href="#badge"/></svg><svg class="card__icon" style="color:#fff"><use href="#i-tick"/></svg><h3 class="card__title">Complete</h3><p class="card__text">Apps with Live TV<br>Catchup TV + VOD<br>Middleware + Ads</p></article>
  <article class="card col2 row1"><svg class="card__frame"><use href="#frame"/></svg><svg class="card__icon"><use href="#badge"/></svg><svg class="card__icon" style="color:#fff"><use href="#i-globe"/></svg><h3 class="card__title">MSO Scale</h3><p class="card__text">Nationwide Distribution<br>Cloud or on premise<br>Distributed head-ends</p></article>
  <article class="card col3 row1"><svg class="card__frame"><use href="#frame"/></svg><svg class="card__icon"><use href="#badge"/></svg><svg class="card__icon" style="color:#fff"><use href="#i-headset"/></svg><h3 class="card__title">Reliable</h3><p class="card__text">24/7 Operation<br>24/7 System Monitoring<br>MPEG Video Inspection</p></article>
  <article class="card col1 row2"><svg class="card__frame"><use href="#frame"/></svg><svg class="card__icon"><use href="#badge"/></svg><svg class="card__icon" style="color:#fff"><use href="#i-shield"/></svg><h3 class="card__title">CAS / DRM</h3><p class="card__text">Hollywood approved<br>Highly secure for<br>IPTV/OTT/DVB systems</p></article>
  <article class="card col2 row2"><svg class="card__frame"><use href="#frame"/></svg><svg class="card__icon"><use href="#badge"/></svg><svg class="card__icon" style="color:#fff"><use href="#i-live"/></svg><h3 class="card__title">Streaming</h3><p class="card__text">High Capacity<br>Edge Caching<br>No 3rd party CDN needed</p></article>
  <article class="card col3 row2"><svg class="card__frame"><use href="#frame"/></svg><svg class="card__icon"><use href="#badge"/></svg><svg class="card__icon" style="color:#fff"><use href="#i-cloudplay"/></svg><h3 class="card__title">Transcoding</h3><p class="card__text">High Quality<br>High Density<br>4K/8K Full HD &amp; SD</p></article>
  <article class="card col1 row3"><svg class="card__frame"><use href="#frame"/></svg><svg class="card__icon"><use href="#badge"/></svg><svg class="card__icon" style="color:#fff"><use href="#i-ad"/></svg><h3 class="card__title">Advertising</h3><p class="card__text">Targeted Ads<br>Ad analytics<br>Advertiser Portal</p></article>
  <article class="card col2 row3"><svg class="card__frame"><use href="#frame"/></svg><svg class="card__icon"><use href="#badge"/></svg><svg class="card__icon" style="color:#fff"><use href="#i-cloudnet"/></svg><h3 class="card__title">Middleware</h3><p class="card__text">Live TV with EPG<br>VOD + CDN<br>Catchup TV</p></article>
  <article class="card col3 row3"><svg class="card__frame"><use href="#frame"/></svg><svg class="card__icon"><use href="#badge"/></svg><svg class="card__icon" style="color:#fff"><use href="#i-sms"/></svg><h3 class="card__title">SMS</h3><p class="card__text">MSO Grade Subscriber<br>Management<br>for IPTV/OTT/DVB</p></article>

  <div class="brand brand--footer"><span>StreamVault</span><span class="brand__dot"></span></div>
  <nav class="nav nav--footer"><span>Products</span><span>Resources</span><span>Contact</span></nav>
  <p class="copyright">Copyright © 2021 All Right Reserved</p>
</section>

</body>
</html>
```